Builders Worksite Corflute Outdoor Sign

We are a building company who are just branching out into new construction. How first new build is our own home which was designed by us and a local architect. We are proud and want to create more advertisement around our business.

We need a corflute sign that can staked outside the construction site and can be seen by people passing by.
Updates

Can we please make the company name and logo bigger (Tidewater Lane Homes) This needs to be the focus. Can we please replace 'Mako' with 'Contact Us on 021-649-3157'

Target Market(s)

Home owners and people wishing to build on lifestyle blocks in New Zealand.

Font styles to use
Sans Serif

Requirements
Must have
• It needs to feature our:
Logo
Company name
Contact name and number - Mako - 0216493157
Landscape NOT portrait.

```html
<!DOCTYPE html>
<html lang="en">
<head>
<meta charset="utf-8">
<title>Tidewater Lane Homes – Worksite Sign</title>
<link href="https://fonts.googleapis.com/css2?family=Jost:wght@300;400&family=Montserrat:wght@700&family=Roboto:wght@900&display=swap" rel="stylesheet">
<style>
  :root {
    --navy: #1a1f30;
    --white: #ffffff;
    --gold: #d9a52b;
    --gold-light: #e8b825;
    --gold-deep: #c9962e;
    --silver: #cbcdd0;
    --grey-text: #7a7a7a;
    --cert-red: #e8402f;
    --backdrop: #e6e6e6;
  }
  * { margin: 0; padding: 0; box-sizing: border-box; }
  html, body {
    width: 1200px; height: 1000px; overflow: hidden;
    background: var(--backdrop);
  }
  .sign {
    position: absolute; left: 40px; top: 66px;
    width: 1120px; height: 867px;
    background: var(--navy);
    overflow: hidden;
  }
  .sign__shapes { position: absolute; inset: 0; width: 100%; height: 100%; }

  .brand__dot {
    position: absolute; left: 498px; top: 120px;
    width: 144px; height: 144px; border-radius: 50%;
    background: var(--gold);
  }
  .brand__name, .brand__sub {
    position: absolute; left: 0; width: 100%; text-align: center;
    font-family: "Jost", sans-serif; font-weight: 400; color: var(--white);
    line-height: 1;
  }
  .brand__name { top: 338px; font-size: 92px; letter-spacing: 0.01em; }
  .brand__sub { top: 466px; font-size: 60px; letter-spacing: 0.62em; text-indent: 0.62em; }

  .contact__icon {
    position: absolute; left: 257px; top: 590px; width: 60px; height: 60px;
  }
  .contact__label {
    position: absolute; left: 130px; width: 324px; top: 662px; text-align: center;
    font-family: "Jost", sans-serif; font-weight: 300; font-size: 40px;
    color: var(--navy); line-height: 1; letter-spacing: 0.01em;
  }
  .contact__number {
    position: absolute; left: 44px; top: 710px;
    font-family: "Roboto", sans-serif; font-weight: 900; font-size: 76px;
    color: var(--navy); line-height: 1; letter-spacing: -0.01em;
    white-space: nowrap;
  }
  .divider {
    position: absolute; left: 581px; top: 699px; width: 2px; height: 95px;
    background: var(--navy);
  }
  .badge-practitioner {
    position: absolute; left: 599px; top: 704px; width: 90px; height: 90px;
    border-radius: 50%; background: var(--navy);
  }
  .badge-shield { position: absolute; left: 702px; top: 709px; width: 69px; height: 90px; }
  .certification {
    position: absolute; left: 786px; top: 714px;
    font-family: "Montserrat", sans-serif; font-weight: 700; font-size: 14.5px;
    line-height: 17px; color: var(--cert-red);
  }
  .certification__lead { color: var(--navy); }

  .services {
    position: absolute; left: 52px; width: 990px; top: 814px;
    list-style: none;
    display: flex; justify-content: space-between; align-items: center;
    font-family: "Montserrat", sans-serif; font-weight: 700; font-size: 31px;
    color: var(--grey-text); line-height: 1;
  }
  .services li { list-style: none; }
  .services__bullet {
    width: 14px; height: 14px; border-radius: 50%; background: var(--gold);
    flex: none;
  }
</style>
</head>
<body>
<main class="sign">
  <svg class="sign__shapes" viewBox="0 0 1732 1341" preserveAspectRatio="none" aria-hidden="true">
    <defs>
      <linearGradient id="goldBand" x1="0" y1="0" x2="1" y2="0">
        <stop offset="0" stop-color="var(--gold-light)"/>
        <stop offset="1" stop-color="var(--gold-deep)"/>
      </linearGradient>
    </defs>
    <polygon points="0,1035 437,840 1130,1016 1732,1172 1732,1341 0,1341" fill="var(--white)"/>
    <polygon points="1130,1016 1732,745 1732,875" fill="var(--silver)"/>
    <polygon points="1130,1016 1732,875 1732,1172" fill="url(#goldBand)"/>
  </svg>

  <div class="brand__dot" aria-hidden="true"></div>
  <h1 class="brand__name">TIDEWATER LANE</h1>
  <p class="brand__sub">HOMES</p>

  <svg class="contact__icon" viewBox="0 0 60 60" aria-hidden="true">
    <circle cx="30" cy="30" r="27.5" fill="none" stroke="var(--navy)" stroke-width="3.5"/>
    <path d="M22 19 l5 -2 4 8 -3 3 c1.5 3.5 4 6 7.5 7.5 l3 -3 8 4 -2 5 c-10 1 -23 -12 -22 -22z"
          fill="none" stroke="var(--navy)" stroke-width="2.6" stroke-linejoin="round"/>
    <path d="M33 18 a9 9 0 0 1 9 9 M33 12 a15 15 0 0 1 15 15" fill="none" stroke="var(--navy)" stroke-width="2.6" stroke-linecap="round"/>
  </svg>
  <p class="contact__label">CONTACT US ON</p>
  <p class="contact__number">021-649-3157</p>

  <div class="divider" aria-hidden="true"></div>
  <div class="badge-practitioner" role="img" aria-label="Licensed building practitioner badge"></div>
  <svg class="badge-shield" viewBox="0 0 69 90" role="img" aria-label="Builders association badge">
    <polygon points="0,0 69,0 69,72 34.5,90 0,72" fill="var(--cert-red)"/>
  </svg>
  <p class="certification">
    <span class="certification__lead">CERTIFIED BY</span><br>
    HARBOUR CERTIFIED<br>
    CONSTRUCTION<br>
    ALLIANCE
  </p>

  <ul class="services" aria-label="Services">
    <li class="services__bullet" aria-hidden="true"></li>
    <li>NEW BUILDS</li>
    <li class="services__bullet" aria-hidden="true"></li>
    <li>RENOVATIONS</li>
    <li class="services__bullet" aria-hidden="true"></li>
    <li>EXTENSIONS</li>
    <li class="services__bullet" aria-hidden="true"></li>
    <li>SHEDS</li>
  </ul>
</main>
</body>
</html>
```